HL - business card

Harbor Lane Brokers is an insurance brokerage firm, inovative, proactive, vigorous, which aims to become the leader of the insurance brokers in Anfrica. We should like to get some designs which should be avoided also in Gray / Metallic for the Administration and Orange / Blue for the Managers (ike in the picture sent). The Blue / Green logo is not the correct one, but the source of the file. Please adjust the color accordingly for the business cards. 1 / Orange / Blue 2 / Gray / Metallic We want something classic but which is transmitted strenght, inovation, modernity and most of all, rapidity. We want something start-up like, very punchy and catching eye remaining profesional at the same time. Name: Tobias Wendell Function: Managing Director Address: N ° 17/18 Rua Dovel - R / C 2B Direita - Bairro Sambelo - Luanda Tel: (+244) 947 385 610 Email: tobias.wendell@harbor-l.com Website: www.harbor-l. com We want classic in the front and creative, colorfull at the back. The cards will be printed in relief, with very high quality of paper.
Insurance Broker
Designer to choose colors to be used in the design.

```html
<!DOCTYPE html>
<html lang="en">
<head>
<meta charset="utf-8">
<title>HL - business card</title>
<link rel="stylesheet" href="https://fonts.googleapis.com/css2?family=Lato:wght@400;700;900&display=swap">
<style>
  :root {
    --brand-blue: #0a78c2;
    --accent-red: #e0312a;
    --accent-orange: #f08a3c;
    --paper: #ffffff;
    --backdrop: #2b2e33;
  }
  * { margin: 0; padding: 0; box-sizing: border-box; }
  html, body { width: 1200px; height: 1000px; overflow: hidden; }
  body {
    background: var(--backdrop);
    font-family: "Lato", sans-serif;
    position: relative;
  }
  .card {
    position: absolute;
    left: 220px;
    width: 760px;
    height: 434px;
    border-radius: 22px;
    overflow: hidden;
    box-shadow: 0 12px 30px rgba(0,0,0,0.45);
  }
  .card-back { top: 40px; background: var(--brand-blue); color: var(--paper); }
  .card-front { top: 520px; background: var(--paper); }

  .back-brand {
    position: absolute; top: 170px; left: 0; right: 0;
    display: flex; align-items: center; justify-content: center; gap: 16px;
  }
  .brand-dot {
    width: 34px; height: 34px; border-radius: 50%;
    border: 4px solid var(--paper);
  }
  .back-brand .brand-name {
    font-weight: 900; font-size: 40px; letter-spacing: 1px; text-transform: uppercase;
  }
  .back-web {
    position: absolute; top: 320px; left: 0; right: 0; text-align: center;
    font-size: 20px; letter-spacing: 0.5px;
  }

  .front-wave { position: absolute; inset: 0; }
  .front-brand {
    position: absolute; top: 120px; right: 42px;
    display: flex; align-items: center; gap: 12px;
  }
  .front-brand .brand-dot { border-color: var(--accent-orange); width: 30px; height: 30px; }
  .front-brand .brand-name {
    font-weight: 900; font-size: 32px; letter-spacing: 0.5px;
    color: var(--brand-blue); text-transform: uppercase;
  }
  .person { position: absolute; left: 60px; top: 188px; color: var(--paper); }
  .person-name { font-weight: 900; font-size: 30px; color: var(--accent-red); letter-spacing: 1px; }
  .person-role { font-size: 19px; margin-top: 2px; }
  .contact-list { list-style: none; margin-top: 18px; }
  .contact-list li {
    display: flex; align-items: center; gap: 12px;
    font-size: 19px; line-height: 31px;
  }
  .contact-icon { width: 16px; height: 16px; flex: none; }
  .address {
    position: absolute; right: 42px; bottom: 26px;
    text-align: right; color: var(--paper); font-size: 19px; line-height: 27px;
  }
</style>
</head>
<body>

  <section class="card card-back">
    <div class="back-brand">
      <span class="brand-dot"></span>
      <span class="brand-name">Harbor Lane Brokers</span>
    </div>
    <p class="back-web">www.harbor-l. com</p>
  </section>

  <section class="card card-front">
    <svg class="front-wave" viewBox="0 0 760 434" width="760" height="434" aria-hidden="true">
      <defs>
        <linearGradient id="stripe-fade" x1="0" x2="1" y1="0" y2="0">
          <stop offset="0" stop-color="#e0312a"/>
          <stop offset="1" stop-color="#f08a3c"/>
        </linearGradient>
      </defs>
      <path d="M0,160 C220,140 330,190 430,270 C520,340 620,352 760,337"
            fill="none" stroke="url(#stripe-fade)" stroke-width="9"/>
      <path d="M0,174 C220,154 330,204 430,284 C520,354 620,366 760,351 L760,434 L0,434 Z"
            fill="#0a78c2"/>
    </svg>

    <div class="front-brand">
      <span class="brand-dot"></span>
      <span class="brand-name">Harbor Lane Brokers</span>
    </div>

    <div class="person">
      <h1 class="person-name">Tobias Wendell</h1>
      <p class="person-role">Managing Director</p>
      <ul class="contact-list">
        <li>
          <svg class="contact-icon" viewBox="0 0 16 16"><path d="M3 1 L6 1 L7 5 L5 6.5 C6 9 7.5 10.5 9.5 11 L11 9 L15 10 L15 13 C15 14 14 15 13 15 C6.5 14.5 1.5 9.5 1 3 C1 2 2 1 3 1 Z" fill="#e8512e"/></svg>
          <span>(+244) 947 385 610</span>
        </li>
        <li>
          <svg class="contact-icon" viewBox="0 0 16 16"><rect x="1" y="3" width="14" height="10" rx="1" fill="none" stroke="#e8512e" stroke-width="1.6"/><path d="M1.5 4 L8 9 L14.5 4" fill="none" stroke="#e8512e" stroke-width="1.6"/></svg>
          <span>tobias.wendell@harbor-l.com</span>
        </li>
        <li>
          <svg class="contact-icon" viewBox="0 0 16 16"><circle cx="8" cy="8" r="6.5" fill="none" stroke="#e8512e" stroke-width="1.6"/><ellipse cx="8" cy="8" rx="3" ry="6.5" fill="none" stroke="#e8512e" stroke-width="1.2"/><path d="M1.5 8 H14.5" stroke="#e8512e" stroke-width="1.2"/></svg>
          <span>www.harbor-l. com</span>
        </li>
      </ul>
    </div>

    <p class="address">N ° 17/18 Rua Dovel - R / C 2B<br>Direita - Bairro Sambelo - Luanda</p>
  </section>

</body>
</html>
```